Events company needs professional workshop flyer design

We need a flyer design to advertise a workshop we are holding. The workshop is for professionals (Speech Pathologists, teachers, Psychologists).

I have attached a flyer with all the information in it. We need the flyer to look modern, and attract the attention of teachers to read it, to encourage them to attend a course to further their knowledge and skills.

It needs to list (as per flyer attached):
- The title of the workshop "Bright Horizons Forward:Growing Voices Together Always. Listen - Build - Rise
- Presented by Professor Maren Holt-Avery (Speech & Language Therapist) & Professor Samuel Pryce (Developmental Psychologist)
- The 4 separate locations it is being held (with dates, and addresses)
- A section for intro of "expert speakers...etc"
- A section for topics to be covered
- A section for learning outcomes of the workshop
- Price
- Registration methods
- Who should attend the workshop
- Bio's of both speakers

It needs to be an A4 vertical brochure that is double sided.

```html
<!DOCTYPE html>
<html lang="en">
<head>
<meta charset="utf-8">
<title>Bright Horizons Forward – Workshop Flyer</title>
<link href="https://fonts.googleapis.com/css2?family=Tinos:ital,wght@0,400;0,700;1,400;1,700&family=Oswald:wght@500&family=Open+Sans:wght@700&display=swap" rel="stylesheet">
<style>
:root{
  --lime:#a6c13a;
  --lime-text:#9cba2c;
  --slate:#6e7fc2;
  --band-grey:#6a6a6a;
  --panel-line:#c9c9c9;
  --ink:#222222;
  --muted:#555555;
  --backdrop:#d9d9d7;
  --paper:#ffffff;
}
*{box-sizing:border-box;margin:0;padding:0}
html,body{width:1200px;height:900px;overflow:hidden}
body{background:var(--backdrop);font-family:"Tinos",serif;color:var(--ink);position:relative}
.page{position:absolute;top:33px;width:533px;height:750px;background:var(--paper);box-shadow:0 2px 8px rgba(0,0,0,.18);overflow:hidden}
.page--front{left:43px}
.page--back{left:623px}
.abs{position:absolute}

.brand{display:flex;align-items:center;gap:5px;font-family:"Open Sans",sans-serif;font-weight:700;font-size:13px;color:var(--slate);letter-spacing:.3px}
.brand__dot{width:11px;height:11px;border-radius:50%;background:var(--lime)}

/* front */
.title-block{left:18px;top:16px;width:375px;text-align:center}
.title-block h1{font-size:19.5px;line-height:22px;font-weight:700}
.title-block .tagline{font-size:13px;font-weight:700;margin-top:3px}
.title-block .presenters{font-size:12px;line-height:14px;color:var(--muted);margin-top:3px}
.front-brand{left:402px;top:30px}
.price-tag{left:397px;top:56px;width:132px;height:98px;background:var(--slate);color:#fff;text-align:center;padding-top:4px}
.price-tag .amount{font-size:17px;font-weight:700}
.price-tag .note{font-size:9.5px;line-height:10.5px;margin-top:1px}
.price-tag .year{position:absolute;right:5px;bottom:0;font-family:"Open Sans",sans-serif;font-size:21px;font-weight:700}
.venues{left:0;top:154px;width:533px;display:grid;grid-template-columns:repeat(4,1fr)}
.venue__head{background:var(--lime);color:#fff;height:53px;padding:4px 8px;border-right:2px solid #fff}
.venue__city{font-size:13px;font-weight:700}
.venue__date{font-size:11.5px;font-weight:700;line-height:13px}
.venue__days{font-size:8.5px;font-weight:700}
.venue__place{height:41px;padding:6px 8px 0;font-size:9px;line-height:10.5px}
.rule-lime{left:0;top:248px;width:533px;height:3px;background:var(--lime)}
.intro{left:30px;top:256px;width:478px;font-size:12.5px;font-weight:700;line-height:14px}
.details{left:38px;top:306px;width:460px;font-size:10.3px;line-height:12.4px;color:#333}
.details p{margin-bottom:8px}
.details ul{list-style:none;margin-bottom:8px}
.details li::before{content:". "}
.foot-band{left:0;bottom:0;width:533px;height:21px;background:var(--lime)}

/* back */
.back-brand{left:20px;top:41px}
.section-tab{left:150px;top:32px;width:100px;height:35px;background:var(--slate);color:#fff;font-family:"Open Sans",sans-serif;font-weight:700;font-size:23px;line-height:35px;text-align:center}
.photo--one{left:19px;top:105px;width:99px;height:69px;background:linear-gradient(135deg,#8a8a8a,#3a3a3a)}
.photo--two{left:19px;top:242px;width:99px;height:99px;background:linear-gradient(135deg,#bcbcbc,#6a6a6a)}
.bio{left:127px;width:392px;font-size:10.3px;line-height:12.8px;text-align:justify}
.bio h2{font-size:11.5px;font-weight:700;margin-bottom:1px}
.bio--one{top:88px}
.bio--two{top:230px}
.divider{left:14px;top:357px;width:505px;height:1px;background:var(--panel-line)}
.audience-label{left:0;top:362px;width:533px;text-align:center;font-style:italic;font-size:19px;color:var(--muted)}
.audience{left:0;top:386px;width:533px;text-align:center;font-size:17px;font-weight:700;line-height:20px}
.col-title{top:476px;font-family:"Oswald",sans-serif;font-size:25px;color:var(--lime-text);line-height:27px}
.col-title--cost{left:62px}
.col-title--reg{left:268px}
.info-band{left:0;top:503px;width:533px;height:119px;background:var(--band-grey);color:#fff;display:grid;grid-template-columns:194px 1fr}
.cost{border-right:1px solid #999;text-align:center;padding-top:6px}
.cost .amount{font-size:16px;border-bottom:1px solid #fff;padding-bottom:3px;margin:0 10px 5px}
.cost .note{font-size:10.5px;line-height:12px;padding:0 14px}
.cost .small{font-size:7px;font-style:italic;margin-top:5px;line-height:9px}
.register{text-align:center;padding-top:6px;font-size:8px;line-height:11.5px}
.register .big{font-size:12px;font-weight:700;line-height:15px}
.policy{left:14px;top:655px;width:505px;font-size:8px;line-height:10px}
.policy p{margin-bottom:6px}
</style>
</head>
<body>

<section class="page page--front">
  <div class="abs title-block">
    <h1>Bright Horizons Forward:<br>Growing Voices Together Always</h1>
    <p class="tagline">Listen - Build - Rise</p>
    <p class="presenters"><em>Presented by</em><br>Professor Maren Holt-Avery (Speech &amp; Language Therapist)<br>&amp;<br>Professor Samuel Pryce (Psychologist).</p>
  </div>

  <div class="abs brand front-brand"><span class="brand__dot"></span>WORDWISE</div>

  <div class="abs price-tag">
    <p class="amount">2 days: $495</p>
    <p class="note">(Earlybird)<br>Add an additional $88<br>if registering within 3<br>weeks of workshop</p>
    <span class="year">2015</span>
  </div>

  <div class="abs venues">
    <div><div class="venue__head"><p class="venue__city">Brisbane</p><p class="venue__date">9th-10th February</p><p class="venue__days">(Monday-Tuesday)</p></div><p class="venue__place">Ridgeview Community Club<br>42 Harlow Rd, Ashgrove</p></div>
    <div><div class="venue__head"><p class="venue__city">Sydney</p><p class="venue__date">12th-13th February</p><p class="venue__days">(Thursday-Friday)</p></div><p class="venue__place">Lakeside Function Centre<br>Cnr Alder St and Brook Rd,<br>Kingsford</p></div>
    <div><div class="venue__head"><p class="venue__city">Melbourne</p><p class="venue__date">5th-6th March</p><p class="venue__days">(Thursday-Friday)</p></div><p class="venue__place">Parkline Hotel<br>27-31 Carden St,<br>Melbourne</p></div>
    <div><div class="venue__head" style="border-right:0"><p class="venue__city">Perth</p><p class="venue__date">17th -18th March</p><p class="venue__days">(Tuesday-Wednesday)</p></div><p class="venue__place">Harbourlight Perth<br>8 Marlow Ave,<br>Northbridge</p></div>
  </div>
  <div class="abs rule-lime"></div>

  <p class="abs intro">Expert International Speakers, Speech Language Therapist <em>Maren Holt-Avery</em> and Developmental Psychologist <em>Dr Samuel Pryce</em> are coming to Australia in February and March 2015.</p>

  <div class="abs details">
    <p>Limited places are available for their two day event focusing on language difficulties in children. Professors Holt-Avery and Pryce are world leading scientists who bring years of expertise and their specific interest in both clinical practice and research. They will share their knowledge with you and use videos, case studies and discussions to develop your practical skills and strategies to use in the clinical setting and classroom.</p>
    <p>Topics to be covered include:</p>
    <ul>
      <li>Language Difficulties - terminology, diagnosis, assessment &amp; intervention strategies</li>
      <li>Autism Spectrum Disorders (ASD) and language difficulties—Links, overlaps and differences</li>
      <li>Developmental trajectories—How language difficulties change from childhood to adolescence</li>
      <li>The IQ problem: Nonverbal skills in children with Language difficulties</li>
      <li>Social, emotional and behavioural difficulties: Problems at different stages of development for children with language difficulties.</li>
      <li>TABLETS/APPS/New media and children with Language difficulties— what do they mean for these children.</li>
    </ul>
    <p>Learning outcomes of the workshop:</p>
    <ul>
      <li>To build a developmental framework for assessment and intervention of language difficulties from early childhood to adolescence.</li>
      <li>To know what are the red flags that need to be targets of intervention</li>
      <li>To determine the key principles that identify and differentiate Language difficulties vs ASD in early childhood, middle childhood and adolescence.</li>
      <li>To predict who is most at risk of social, emotional and behavioural difficulties and learn what to target in intervention, with whom, and why</li>
      <li>To understand the impact of the digital world for language, literacy and educational attainment</li>
      <li>To know the benefits of professional therapy, and how you can shift the educational outcomes of young people with language difficulties.</li>
    </ul>
  </div>
  <div class="abs foot-band"></div>
</section>

<section class="page page--back">
  <div class="abs brand back-brand"><span class="brand__dot"></span>WORDWISE</div>
  <div class="abs section-tab">ABOUT</div>

  <div class="abs photo--one" role="img" aria-label="Portrait photograph of Professor Maren Holt-Avery"></div>
  <div class="abs bio bio--one">
    <h2>Professor Maren Holt-Avery</h2>
    <p>Maren is Professor of Child Language and Learning at the University of Northvale, UK. She is the director of a nationwide longitudinal study on specific language impairment (SLI) that has been following individuals from 7 years of age to adult life. Maren has an interest in the interface between clinical practice and research. She is founder member of the SPARK campaign to raise awareness of SLI (www.sparkvoices.org/campaign), was editor of the Journal of Language and Communication Needs and was involved in the development of national clinical guidelines for language disorders in children.</p>
  </div>

  <div class="abs photo--two" role="img" aria-label="Portrait photograph of Professor Samuel Pryce"></div>
  <div class="abs bio bio--two">
    <h2>Professor Samuel Pryce</h2>
    <p>Samuel Pryce is Professor of Psychology at the University of Kelmore, UK. He has previously held a Chair at the University of Westhaven and was Director of the UWH Child Development Centre. He has a longestablished interest in language difficulties and child development. He has written a large number of journal articles and books for academics and practitioners, and is editor of the journal Early Words Quarterly. For the past ten years he has been co-directing the longitudinal study of SLI with Maren Holt-Avery.</p>
  </div>

  <div class="abs divider"></div>
  <p class="abs audience-label">Who should attend?</p>
  <p class="abs audience">For Teachers, Speech Pathologists, Psychologists and<br>those interested in learning more about<br>children with Language Learning difficulties</p>

  <h3 class="abs col-title col-title--cost">COST</h3>
  <h3 class="abs col-title col-title--reg">TO REGISTER</h3>
  <div class="abs info-band">
    <div class="cost">
      <p class="amount">2 days: $495</p>
      <p class="note">(Earlybird)<br>Add an additional $88 if registering within 3 weeks of workshop.</p>
      <p class="small">(incl G.S.T, workshop materials,<br>morning and afternoon tea, lunch)</p>
    </div>
    <div class="register">
      <p>online at</p>
      <p class="big">http://www.wordwisespeech.com.au/events/</p>
      <p>or Call Nora Bellamy on</p>
      <p class="big">02 4000 1234</p>
      <p>or email</p>
      <p class="big">events@wordwisespeech.com.au</p>
      <p>for invoicing for your school or workplace</p>
    </div>
  </div>

  <div class="abs policy">
    <p><strong>Cancellation Policy</strong> - in the event that a participant cancels, The registration fee minus a 10% processing fee ($49.50) will be refunded until Thursday 22nd January 2015. After this date, there will be no refund.</p>
    <p>If the hosts cancel (Wordwise Speech Pathology), or defers the event, 100% of the registration fee will be refunded if the registrant cannot attend on the revised dates, however the hosts bear no responsibility for any costs incurred (such as flights, accommodation, travel expenses) or loss of income.</p>
  </div>
  <div class="abs foot-band"></div>
</section>

</body>
</html>
```